New Design for Accounting Firm

CLIENT NAME: Corvantis
CURRENT WEBSITE: www.corvantisgroup-example.com.au

CLIENTS THE CLIENT LIKES:
http://velmarook.example.se/
http://www.tralvexio.example.biz/index.php
http://www.brindlequo.example.co.uk/
http://www.nerovaskellintrust.example.org/

COLOUR THEMES:
Colour theme to reflect the logo, with a leaning to blue in Accounting & Audit sections and green in Super section.

LOOK AND FEEL:
The look and feel needs to reflect an accessible culture and contemporary sensibility while still communicating our experience and stability as a professional company.

ABOUT:
The concept of 'Corvantis' is integral to our identity. Definition: 'The connection of creative ideas from a group of diverse individuals, applied with the end aim of solving practical problems'. See ''About Us'' on our website for more.

OTHER DETAILS:
Our three divisions (and service areas within each division) must be easily navigated as they related to very different users of the site. Two client sign in sections (Accounting & Super) must be easily distinguished to avoid user confusion.

MENU STRUCTURE:
* About
- includes history, values, our people, community etc
* Accounting & Advisory
- About
- Services
- Tax & Accounting
- Business Advisory
- Family Wealth Management
- Client Sign In
- Calculators
* Audit & Assurance
- About
- Services
* Corvantis Super
- About
- Individuals
- Services
- Advisers
- Services
- Portal Sign In
- Calculators
* Careers
* Newsletters
* Contact

REQUIREMENTS:
- Layered PSD form home and content pages
- No coding required, we use our own CMS to insert XHTML files into.
Updates

Hi Guys,

The client has asked for a non-cliche'd images in the design. If you'd like to try again with some images that represent the business but aren't your standard boring accounting-looking people, then please do! Cliche is a killer in design - please pump some creativity in!

Cheers,
Ted.

Reason: GUYS - PLEASE LISTEN TO THESE COMMENTS - I'VE SAID THEM TWICE NOW AND PEOPLE ARE STILL POSTING PROJECTS WITH CLICHED AND OBVIOUS ACCOUTNING TYPE IMAGES. USE YOUR CREATIVITY AND POST A DESIGN THAT IS OUTSIDE THE BOX WITH REGARDS TO THE IMAGES YOU ARE USING.

Reason: I am waiting to hear back from the client on their decision.

```html
<!DOCTYPE html>
<html lang="en">
<head>
<meta charset="utf-8">
<title>Corvantis — Faceted Financial Services Firm</title>
<link rel="stylesheet" href="https://fonts.googleapis.com/css2?family=Open+Sans:wght@400;600;700&family=PT+Sans+Narrow&family=Roboto+Slab:wght@700&family=Arimo:wght@400;700&display=swap">
<style>
:root{
  --blue:#1a5fa6;
  --blue-dark:#0f4f94;
  --green:#3f8f2a;
  --green-bright:#6cc24a;
  --green-tab:#5cb848;
  --ink:#333;
  --muted:#555;
  --black:#050505;
  --footer:#2a2a2a;
  --footer-line:#3c3c3c;
  --footer-text:#bdbdbd;
  --field:#3a3a3a;
}
*{box-sizing:border-box;margin:0;padding:0}
html,body{width:822px;height:1200px;overflow:hidden;background:#fff}
body{position:relative;font-family:"Open Sans",Verdana,sans-serif;color:var(--ink)}
.abs{position:absolute}

/* header */
.site-header{left:0;top:0;width:822px;height:104px;background:linear-gradient(180deg,#e8eef3 0%,#fff 60%)}
.brand{left:70px;top:34px;display:flex;align-items:center;gap:10px}
.brand-mark{width:36px;height:36px;background:var(--blue)}
.brand-name{font-family:"Open Sans",sans-serif;font-size:40px;font-weight:400;color:var(--blue);letter-spacing:-1px;line-height:1}
.login-box{left:638px;top:22px;width:115px;height:46px;background:#fff;border:1px solid #dde3e8;border-radius:3px;box-shadow:0 1px 3px rgba(0,0,0,.1);font-family:Arimo,Arial,sans-serif;font-size:8.3px;font-weight:700;color:var(--blue);text-align:right;padding:2px 7px 0 0;line-height:20px;white-space:nowrap}
.login-box span{display:block}
.login-box span+span{border-top:1px solid #e6e6e6}

/* nav */
.nav-band{left:0;top:104px;width:822px;height:91px;background:var(--black)}
.tab{top:98px;height:26px;background:linear-gradient(#6fc957,#49a43a);border-radius:3px;color:#fff;font-family:Arimo,Arial,sans-serif;font-size:8.5px;font-weight:700;display:flex;align-items:center;justify-content:center}
.tab-careers{left:604px;width:52px}
.tab-news{left:678px;width:70px}
.main-nav{right:69px;top:144px;font-family:Arimo,Arial,sans-serif;font-weight:700;font-size:10px;color:#fff;white-space:nowrap}
.main-nav .sep{margin:0 6px}
.main-nav .current{color:var(--green-bright);text-decoration:underline}
.nav-rule{left:0;top:168px;width:822px;height:1px;background:var(--green)}
.util-nav{left:654px;top:172px;font-size:8px;color:#888}
.util-nav .sep{margin:0 8px}
.dropdown{left:386px;top:165px;width:110px;background:#62bd55;border-radius:0 0 5px 5px;box-shadow:0 2px 4px rgba(0,0,0,.3);padding-bottom:4px}
.dropdown li{list-style:none;font-family:Arimo,Arial,sans-serif;font-size:7px;color:#fff;height:15.2px;line-height:15px;padding-left:5px;border-bottom:1px solid #7fd070;white-space:nowrap}
.dropdown li:last-child{border-bottom:none}

/* hero */
.hero{left:0;top:195px;width:822px;height:300px;background:#fff}
.hero-title{left:70px;top:238px;font-family:"Roboto Slab",Georgia,serif;font-weight:700;font-size:37px;color:var(--blue-dark);letter-spacing:.5px;line-height:1}
.hero-sub{left:70px;top:288px;font-family:"PT Sans Narrow",sans-serif;font-size:27px;color:#222;line-height:1;white-space:nowrap}
.hero-lead{left:71px;top:324px;font-size:13px;font-weight:700;color:#222}
.hero-lead2{left:71px;top:344px;font-size:11px;color:#333}
.hero-note{left:72px;top:369px;width:290px;font-size:9.5px;color:var(--blue);line-height:12px}
.btn-readmore{left:70px;top:408px;width:77px;height:26px;border:2px solid #d6dcd4;border-radius:3px;background:#fafafa;color:var(--green);font-size:10px;display:flex;align-items:center;justify-content:center;box-shadow:0 1px 2px rgba(0,0,0,.1)}
.hero-art{left:436px;top:205px;width:296px;height:285px;background:radial-gradient(ellipse at 55% 60%,#6fb1ea 0%,#b9d9f2 45%,#fff 75%)}
.slider-dots{left:698px;top:474px;width:52px;height:13px;border-radius:3px;background:#e4e4e4;display:flex;gap:3px;align-items:center;justify-content:center}
.slider-dots i{width:6px;height:6px;border-radius:50%;background:#aaa}
.slider-dots i:first-child{background:#7cb342}
.hero-base{left:0;top:494px;width:822px;height:11px;background:#111}

/* features */
.features{left:0;top:505px;width:822px;height:208px;background:linear-gradient(#fff,#f0f0f0)}
.feature{top:515px;width:172px;text-align:center}
.feature-icon{width:100px;height:88px;margin:0 auto;border-radius:8px}
.feature h3{font-family:Arimo,Arial,sans-serif;font-size:13px;font-weight:700;color:var(--green);margin-top:18px;white-space:nowrap}
.feature p{font-size:7.8px;color:var(--muted);line-height:14px;margin:8px auto 0;width:158px;height:28px;overflow:hidden;text-align:justify;text-align-last:center}
.feature .more{display:inline-block;margin-top:9px;width:76px;height:18px;border:2px solid #c9ced2;border-radius:3px;background:#fff;font-family:"Roboto Slab",Georgia,serif;font-size:7px;color:var(--blue);line-height:14px}
.f1{left:68px}.f2{left:245px}.f3{left:413px}.f4{left:591px}
.col-rule{top:512px;width:1px;height:180px;background:linear-gradient(transparent,#e2e2e2,transparent)}

/* welcome */
.welcome-title{left:88px;top:750px;font-family:Arimo,Arial,sans-serif;font-weight:700;font-size:13px;color:var(--blue-dark);letter-spacing:.3px}
.copy{left:88px;width:645px;font-size:7.8px;color:#444;line-height:12.5px}
.divisions{left:90px;top:840px;list-style:none}
.divisions li{font-size:9px;color:var(--green);text-decoration:underline;height:18.5px;display:flex;align-items:center;gap:6px}
.divisions li::before{content:"";width:6px;height:6px;border-radius:50%;background:radial-gradient(#8bc34a,#3f7a1f)}
.page-rule{left:0;top:967px;width:822px;height:2px;background:#eee}

/* footer */
.site-footer{left:0;top:985px;width:822px;height:215px;background:var(--footer)}
.footer-brand{left:70px;top:1033px;display:flex;align-items:center;gap:10px;opacity:.55}
.footer-brand .brand-mark{background:#5a5a5a}
.footer-brand .brand-name{color:#5a5a5a}
.f-col{top:1021px;font-family:Arimo,Arial,sans-serif}
.f-col h4{font-size:8.5px;font-weight:700;color:#eee;letter-spacing:.5px;white-space:nowrap}
.field{width:126px;height:20px;margin-top:11px;background:var(--field);border-radius:2px;box-shadow:inset 0 1px 2px rgba(0,0,0,.5);font-size:8px;color:#999;padding-left:4px;line-height:20px}
.field:first-of-type{margin-top:17px}
.f-row{display:flex;align-items:center;justify-content:space-between;width:126px;margin-top:8px;font-size:6.5px;color:#888}
.signin{width:50px;height:15px;background:#333;border-radius:2px;color:#ddd;font-size:8px;font-weight:700;text-align:center;line-height:15px;box-shadow:0 1px 2px rgba(0,0,0,.6)}
.fc1{left:327px}.fc2{left:484px}.fc3{left:635px}
.footer-nav{list-style:none;margin-top:14px}
.footer-nav li{font-size:8px;color:var(--footer-text);line-height:12.5px;white-space:nowrap}
.f-div{top:1030px;width:1px;height:84px;background:var(--footer-line)}
.footer-base{left:0;top:1146px;width:822px;height:1px;background:var(--footer-line)}
.copyright{right:72px;top:1154px;font-size:7.8px;color:#bbb}
</style>
</head>
<body>

<header class="abs site-header"></header>
<div class="abs brand"><span class="brand-mark"></span><span class="brand-name">Corvantis</span></div>
<div class="abs login-box"><span>Accounting&nbsp; Log In</span><span>Corvantis Super Log In</span></div>

<div class="abs nav-band"></div>
<div class="abs tab tab-careers">Careers</div>
<div class="abs tab tab-news">Newsletters</div>
<nav class="abs main-nav">Home<span class="sep">|</span>About<span class="sep">|</span><span class="current">Accounting &amp; Advisory</span><span class="sep">|</span>Audit &amp; Assurance<span class="sep">|</span>Corvantis Super<span class="sep">|</span>Contact Us</nav>
<div class="abs nav-rule"></div>
<div class="abs util-nav">Useful Links<span class="sep">|</span>Sitemap</div>

<section class="abs hero"></section>
<h1 class="abs hero-title">CORVANTIS</h1>
<p class="abs hero-sub">FACETED FINANCIAL SERVICES FIRM</p>
<p class="abs hero-lead">incorporating the skills of accountants</p>
<p class="abs hero-lead2">business advisers, auditors and SMSF specialists</p>
<p class="abs hero-note">Corvantis is a Tasmanian based firm which offers the skills of Accountants.</p>
<div class="abs btn-readmore">READMORE</div>
<div class="abs hero-art" role="img" aria-label="Illustration of a team standing on blue city blocks beside a rising green arrow"></div>
<div class="abs slider-dots"><i></i><i></i><i></i><i></i><i></i></div>
<div class="abs hero-base"></div>

<ul class="abs dropdown">
  <li>About</li><li>Services</li><li>Tax &amp; Accounting</li><li>Business Advisory</li><li>Family Wealth Management</li><li>Client Sign In</li>
</ul>

<section class="abs features"></section>
<div class="abs col-rule" style="left:241px"></div>
<div class="abs col-rule" style="left:419px"></div>
<div class="abs col-rule" style="left:586px"></div>

<article class="abs feature f1">
  <div class="feature-icon" role="img" aria-label="Illustration of a banded stack of banknotes" style="background:linear-gradient(135deg,#cfd8c4,#8ea67c)"></div>
  <h3>Accounting &amp; Tax</h3>
  <p>Our Accounting and Advisory team - AG Corvantis Chartered Accountants.</p>
  <span class="more">READ MORE</span>
</article>
<article class="abs feature f2">
  <div class="feature-icon" role="img" aria-label="Illustration of a gold wall clock" style="background:radial-gradient(circle,#fff 30%,#f2c24a 55%,#fff 72%)"></div>
  <h3>Audit &amp; Assurance</h3>
  <p>While the number of firms providing audit services has decreased in recent</p>
  <span class="more">READ MORE</span>
</article>
<article class="abs feature f3">
  <div class="feature-icon" role="img" aria-label="Illustration of a rising coloured bar chart" style="background:linear-gradient(90deg,#e74c3c,#f39c12,#7dc142)"></div>
  <h3>Corvantis Super</h3>
  <p>Corvantis Super is a specialist division formed in July 2009 to specifically</p>
  <span class="more">READ MORE</span>
</article>
<article class="abs feature f4">
  <div class="feature-icon" role="img" aria-label="Illustration of two business advisers" style="background:linear-gradient(#d9c1a5,#2e2e2e)"></div>
  <h3>Business Advisory</h3>
  <p>Corvantis's specialist advisers focus on services and advice that</p>
  <span class="more">READ MORE</span>
</article>

<h2 class="abs welcome-title">WELCOME TO CORVANTIS</h2>
<p class="abs copy" style="top:786px">Corvantis is a Tasmanian based firm which offers the skills of Accountants, Business Performance Advisers, Auditors and Self Managed Super Fund Specialists.</p>
<p class="abs copy" style="top:811px">From our offices in Devonport and Hobart we deliver services across three divisions:</p>
<ul class="abs divisions">
  <li>AG Corvantis Chartered Accountants</li>
  <li>Corvantis Audit &amp; Assurance</li>
  <li>Corvantis Super</li>
</ul>
<p class="abs copy" style="top:903px">Through our three divisions, our clients benefit from the application of specialist skills and systems, developed in relevant areas of expertise. At the same time, our teams are skilled at integrating their knowledge with the common goal of meeting our clients' comprehensive needs.</p>
<div class="abs page-rule"></div>

<footer class="abs site-footer"></footer>
<div class="abs brand footer-brand"><span class="brand-mark"></span><span class="brand-name">Corvantis</span></div>
<div class="abs f-div" style="left:308px"></div>
<div class="abs f-div" style="left:465px"></div>
<div class="abs f-div" style="left:622px"></div>
<div class="abs f-div" style="left:748px"></div>

<div class="abs f-col fc1">
  <h4>Accounting&nbsp; Log In</h4>
  <div class="field">Username</div>
  <div class="field">Password</div>
  <div class="f-row"><span>Forgot password?</span><span class="signin">Sign In</span></div>
</div>
<div class="abs f-col fc2">
  <h4>Corvantis Super Log In</h4>
  <div class="field">Username</div>
  <div class="field">Password</div>
  <div class="f-row"><span>Forgot password?</span><span class="signin">Sign In</span></div>
</div>
<div class="abs f-col fc3">
  <h4>Navigation</h4>
  <ul class="footer-nav">
    <li>Home</li><li>About</li><li>Accounting &amp; Advisory</li><li>Audit &amp; Assurance</li><li>Corvantis Super</li><li>Contact Us</li>
  </ul>
</div>
<div class="abs footer-base"></div>
<p class="abs copyright">© 2011 Corvantis Group | Return to Top of Page | Privacy Policy</p>

</body>
</html>
```